Digital agency needs a new web design

We’re looking to redesign our website – so that it is 3 things: smart, stylish and simplistic.
Plinth are a digital performance agency, offering services in PPC. SEO. Analytics, Display, Content and Paid Social, and we work with fantastic clients.
Our current website isn't reflective of how forward-thinking we are as an agency, and doesn't convey our two USPs well - our technology and our network of digital marketing experts. So we're looking to build a clear and concise site that attracts both inbound leads and digital marketing professionals to join our team or our Plinthie network.
You can take a look at our current website here - http://plinth-example.net/. The copy will change and we happy for the colours to change.

Target Market(s)

The primary target audience is marketing directors, digital directors, marketing managers and online acquisition managers. The secondary audience are people in the industry looking for work either as permanent employees or as part of the Plinth freelance network.

Industry/Entity Type

Marketing

Number of Pages Required

5+ page

Font styles to use
Sans Serif

Requirements
Must have
• - A stylish/ grown-up feel
• - Be of a design/ templates that can be editable
• - A really clear concise/ homepage
• The homepage must include:
• 1. A reference to our services
• 2. A reference to our network of digital marketing experts
• 3. A reference to our technology
• 4. A section for case studies
• 5. A section for our blog
• 6. A newsletter signup
• Th copy will be changed so please don't feel like you need to keep that.
Should not have
• - Cartoon style images as on the site on the moment
• - You should not have to scroll very far to find out what we do

```html
<!DOCTYPE html>
<html lang="en">
<head>
<meta charset="utf-8">
<title>Plinth – Digital Performance Agency</title>
<link href="https://fonts.googleapis.com/css2?family=Roboto:wght@300;400;500;700&family=Roboto+Condensed:wght@400;700&display=swap" rel="stylesheet">
<style>
:root{
  --blue:#2fb4e2;
  --blue-dark:#1b9ccb;
  --teal:#3ec1c9;
  --yellow:#f7c21a;
  --ink:#3a3a3a;
  --muted:#8a8a8a;
  --light:#f4f5f6;
  --charcoal:#2f3235;
  --charcoal-2:#3b3f43;
  --footer:#42c3cc;
  --footer-dark:#263238;
  --white:#ffffff;
}
*{box-sizing:border-box;margin:0;padding:0}
html,body{width:1200px;height:2564px;overflow:hidden}
body{font-family:'Roboto',Arial,sans-serif;color:var(--ink);background:var(--white);font-size:14px}
.heading{font-family:'Roboto Condensed','Roboto',sans-serif;font-weight:700;text-transform:uppercase}

/* top bar */
.topbar{height:32px;display:flex;align-items:center;justify-content:space-between;padding:0 60px;font-size:12px;color:var(--muted);border-bottom:1px solid #eee}
.topbar .contact{display:flex;gap:24px;align-items:center}
.topbar .contact span{display:flex;align-items:center;gap:6px}
.dots{display:flex;gap:8px}
.dots i{width:16px;height:16px;border-radius:50%;background:#c8cdd1;display:block}

/* header */
.header{height:88px;display:flex;align-items:center;justify-content:space-between;padding:0 60px}
.brand{display:flex;align-items:center;gap:10px;font-size:34px;font-weight:500;color:var(--ink)}
.brand i{width:14px;height:14px;border-radius:50%;background:var(--blue);display:block}
.nav{display:flex;gap:30px;font-size:12px;font-weight:500;text-transform:uppercase}
.nav a{color:var(--ink);text-decoration:none;padding-bottom:6px}
.nav a.active{color:var(--blue);border-bottom:2px solid var(--blue)}

/* hero */
.hero{height:472px;background:linear-gradient(135deg,#38bde8 0%,#2aa9da 55%,#3bbbe6 100%);position:relative;padding:0 60px;display:flex;align-items:center}
.hero-text{width:460px;color:var(--white)}
.hero-text h1{font-size:46px;line-height:1;margin-bottom:6px;white-space:nowrap}
.hero-text p{font-size:26px;line-height:1.2;font-family:'Roboto Condensed',sans-serif;font-weight:700;text-transform:uppercase;margin-bottom:30px}
.btn-yellow{display:inline-block;background:var(--yellow);color:var(--white);font-size:13px;font-weight:700;padding:14px 26px;border-radius:3px;text-transform:uppercase}
.arrows{display:flex;gap:8px;margin-top:20px}
.arrows span{width:26px;height:26px;border-radius:50%;background:rgba(0,0,0,.35);display:flex;align-items:center;justify-content:center}
.hero-art{position:absolute;right:110px;top:50px;width:440px;height:370px;border-radius:10px;background:linear-gradient(160deg,rgba(255,255,255,.15),rgba(220,232,238,.55) 55%,rgba(150,160,168,.45))}

/* welcome */
.welcome{height:280px;text-align:center;padding-top:82px}
.welcome h2{font-size:32px;color:var(--ink);margin-bottom:8px}
.welcome h2 em{font-style:normal;color:var(--blue)}
.rule{width:50px;height:2px;background:var(--blue);margin:0 auto 24px}
.welcome p{width:930px;margin:0 auto;font-size:13px;line-height:1.7;color:var(--muted)}

/* services */
.services{height:328px;background:var(--light);display:flex;justify-content:center;gap:60px;padding-top:40px}
.service{width:180px;text-align:center}
.service .icon{width:104px;height:104px;border-radius:50%;background:var(--teal);margin:0 auto 18px;display:flex;align-items:center;justify-content:center;border:5px solid #dff4f5}
.service h3{font-size:20px;color:var(--ink);margin-bottom:10px}
.service p{font-size:12px;line-height:1.6;color:var(--muted)}

/* technology */
.tech{height:312px;background:linear-gradient(135deg,var(--charcoal-2),var(--charcoal) 60%,#26292c);display:flex;align-items:center;padding:0 60px;gap:80px}
.tech-art{width:420px;height:250px;background:linear-gradient(160deg,#e58a45 0%,#c9cdd0 35%,#9aa0a5 70%,#5a6066 100%);border-radius:4px;opacity:.9}
.tech-text{width:560px;color:var(--white)}
.tech-text h2{font-size:26px;line-height:1.1}
.tech-text h4{font-size:17px;color:#ccd;margin-bottom:14px}
.tech-text p{font-size:12px;line-height:1.7;color:#b8bcc0;margin-bottom:18px}
.btn-outline{display:inline-block;border:1px solid #ccd;color:var(--white);font-size:11px;padding:9px 18px;border-radius:16px;text-transform:uppercase}

/* blog */
.blog{height:520px;text-align:center;padding-top:42px}
.blog h2{font-size:32px;margin-bottom:8px}
.cards{display:flex;justify-content:center;gap:36px;margin-top:12px}
.card{width:300px;text-align:left}
.card .thumb{height:240px;position:relative;margin-bottom:14px}
.card .date{position:absolute;right:0;bottom:0;width:52px;height:58px;background:var(--charcoal);color:var(--white);text-align:center;font-size:12px;padding-top:10px;line-height:1.4}
.card .date b{display:block;font-size:18px}
.card h3{font-size:15px;font-weight:700;margin-bottom:8px}
.card p{font-size:12px;line-height:1.6;color:var(--muted);margin-bottom:6px}
.card a{font-size:12px;color:var(--blue);text-decoration:none}

/* partners */
.partners{height:208px;display:flex;align-items:center;justify-content:center;gap:40px}
.partners i{display:block;background:#d8dcdf}
.partners .sq{width:90px;height:80px;border-radius:4px}
.partners .wide{width:120px;height:46px;border-radius:4px}
.partners .circ{width:70px;height:70px;border-radius:50%}

/* footer */
.footer{height:288px;background:var(--footer);display:flex;padding:52px 60px 0;gap:70px;color:var(--white)}
.footer .brand{color:var(--white);font-size:40px;width:250px;align-self:flex-start}
.footer .brand i{background:var(--white)}
.fcol{width:210px}
.fcol h5{font-size:13px;font-weight:700;text-transform:uppercase;margin-bottom:14px}
.fcol li{list-style:none;font-size:12px;line-height:2}
.fcol p{font-size:12px;line-height:1.8}
.signup{display:flex;margin:14px 0}
.signup span{flex:1;background:var(--white);color:var(--muted);font-size:12px;padding:9px 10px}
.signup b{background:var(--yellow);font-size:12px;padding:9px 12px}
.fdots{display:flex;gap:10px}
.fdots i{width:28px;height:28px;border-radius:50%;background:rgba(255,255,255,.35);display:block}
.copyright{height:36px;background:var(--footer-dark);color:#b0b6ba;font-size:11px;text-align:center;line-height:36px}
</style>
</head>
<body>

<div class="topbar">
  <div class="contact">
    <span><svg width="11" height="11" viewBox="0 0 24 24"><path fill="#8a8a8a" d="M6.6 10.8a15 15 0 0 0 6.6 6.6l2.2-2.2c.3-.3.7-.4 1-.2 1.1.4 2.3.6 3.6.6.6 0 1 .4 1 1V20c0 .6-.4 1-1 1A17 17 0 0 1 3 4c0-.6.4-1 1-1h3.5c.6 0 1 .4 1 1 0 1.3.2 2.5.6 3.6.1.3 0 .7-.2 1z"/></svg>+44 20 0000 0000</span>
    <span><svg width="12" height="10" viewBox="0 0 24 18"><rect x="1" y="1" width="22" height="16" fill="none" stroke="#8a8a8a" stroke-width="2"/><path d="M1 1l11 9 11-9" fill="none" stroke="#8a8a8a" stroke-width="2"/></svg>info@plinth-example.net</span>
  </div>
  <div class="dots"><i></i><i></i><i></i><i></i></div>
</div>

<header class="header">
  <div class="brand"><i></i>Plinth</div>
  <nav class="nav">
    <a class="active">Home</a><a>Services</a><a>About Plinth</a><a>Our Work</a><a>Blog</a><a>Join Us</a><a>Contact</a>
  </nav>
</header>

<section class="hero">
  <div class="hero-text">
    <h1 class="heading">Digital Performance</h1>
    <p>First - we have the only worldwide network of digital specialists</p>
    <span class="btn-yellow">View More</span>
    <div class="arrows">
      <span><svg width="10" height="10" viewBox="0 0 10 10"><path d="M7 1L3 5l4 4" stroke="#fff" stroke-width="2" fill="none"/></svg></span>
      <span><svg width="10" height="10" viewBox="0 0 10 10"><path d="M3 1l4 4-4 4" stroke="#fff" stroke-width="2" fill="none"/></svg></span>
    </div>
  </div>
  <div class="hero-art" role="img" aria-label="Illustration of a laptop with a rocket launching from its screen"></div>
</section>

<section class="welcome">
  <h2 class="heading">Welcome to <em>Plinth</em></h2>
  <div class="rule"></div>
  <p>Our proprietary technology allows for complete visibility on what we're working on. As a client, you can log in to your dashboard whenever you want, before a Monday morning meeting or after a long weekend, to check how things are tracking. We keep everything open, simple and accountable.</p>
</section>

<section class="services">
  <div class="service">
    <div class="icon"><svg width="44" height="44" viewBox="0 0 44 44"><rect x="6" y="8" width="32" height="22" rx="2" fill="none" stroke="#fff" stroke-width="3"/><path d="M16 36h12M22 30v6" stroke="#fff" stroke-width="3"/></svg></div>
    <h3 class="heading">PPC</h3>
    <p>Pay-per-click, PPC advertising, is one of the most effective and accountable ways of marketing.</p>
  </div>
  <div class="service">
    <div class="icon"><svg width="44" height="44" viewBox="0 0 44 44"><circle cx="22" cy="15" r="8" fill="#fff"/><path d="M8 38c0-8 6-13 14-13s14 5 14 13z" fill="#fff"/></svg></div>
    <h3 class="heading">SEO</h3>
    <p>We believe that an organic search presence must intelligent and encompass every part of a brand.</p>
  </div>
  <div class="service">
    <div class="icon"><svg width="44" height="44" viewBox="0 0 44 44"><rect x="10" y="6" width="20" height="26" fill="none" stroke="#fff" stroke-width="3"/><rect x="16" y="12" width="20" height="26" fill="#3ec1c9" stroke="#fff" stroke-width="3"/></svg></div>
    <h3 class="heading">Analytics</h3>
    <p>The automated reporting tool continues to grow and adds depth to every campaign decision.</p>
  </div>
  <div class="service">
    <div class="icon"><svg width="44" height="44" viewBox="0 0 44 44"><rect x="4" y="8" width="36" height="24" rx="2" fill="none" stroke="#fff" stroke-width="3"/><path d="M14 38h16" stroke="#fff" stroke-width="3"/></svg></div>
    <h3 class="heading">Display</h3>
    <p>We can take a complete view of the advertising and publishing channels to reach every user.</p>
  </div>
</section>

<section class="tech">
  <div class="tech-art" role="img" aria-label="Illustration of a desk with keyboard, mouse, coffee cup and stationery"></div>
  <div class="tech-text">
    <h2 class="heading">Third – we glue the whole thing</h2>
    <h4 class="heading">Together with our own technology</h4>
    <p>Our proprietary technology allows for complete visibility on what we're working on. As a client you can log in to your dashboard whenever you want, before a Monday meeting or after a long weekend. We maintain our network in an efficient and smooth way, so we build the functionality to manage all of our work in one platform and report on it instantly.</p>
    <span class="btn-outline">Read More</span>
  </div>
</section>

<section class="blog">
  <h2 class="heading">Latest Blog</h2>
  <div class="rule"></div>
  <div class="cards">
    <article class="card">
      <div class="thumb" role="img" aria-label="Photo of a large event sign in bold letters" style="background:linear-gradient(135deg,#2a6f9e,#d9a441)"><div class="date"><b>23</b>2016</div></div>
      <h3>Plinth At SearchMeet 2016</h3>
      <p>One of our most highlighted topics of the week was our visit and talks.</p>
      <a>Read More »</a>
    </article>
    <article class="card">
      <div class="thumb" role="img" aria-label="Image of a robot figure on a blue background" style="background:linear-gradient(135deg,#5fb3d9,#c9d3da)"><div class="date"><b>18</b>2016</div></div>
      <h3>Tallyframe Insights Launches Automation</h3>
      <p>The new automated insights tool will help teams spot changes sooner than before.</p>
      <a>Read More »</a>
    </article>
    <article class="card">
      <div class="thumb" role="img" aria-label="Image of online shopping icons around a phone" style="background:linear-gradient(135deg,#3fa3d6,#8fd0ec)"><div class="date"><b>12</b>2016</div></div>
      <h3>Swift Pages Evolves To Tackle E-Commerce</h3>
      <p>Faster mobile pages are now arriving for online shops, with new product layouts.</p>
      <a>Read More »</a>
    </article>
  </div>
</section>

<section class="partners" aria-label="Partners and awards">
  <i class="sq"></i><i class="wide"></i><i class="wide"></i><i class="wide"></i><i class="sq"></i><i class="circ"></i><i class="wide"></i>
</section>

<footer class="footer">
  <div class="brand"><i></i>Plinth</div>
  <div class="fcol">
    <h5>Links</h5>
    <ul><li>Latest News</li><li>Case Studies</li><li>Services</li><li>Careers</li><li>Our Network</li><li>Contact Us</li></ul>
  </div>
  <div class="fcol">
    <h5>Get in Touch</h5>
    <p>12 Example Street<br>London, EC1A 0AA<br>+44 20 0000 0000<br>info@plinth-example.net</p>
  </div>
  <div class="fcol">
    <h5>Newsletter</h5>
    <p>Sign up to our newsletter for news and updates.</p>
    <div class="signup"><span>Your email</span><b>Subscribe</b></div>
    <div class="fdots"><i></i><i></i><i></i></div>
  </div>
</footer>
<div class="copyright">Copyright © 2016. All Rights Reserved</div>

</body>
</html>
```